Pediatric Occupational Therapy Brochure Design

This design really needs to stand out, especially with all the wordage that I have included. These brochures will be given to doctors, future clients, and caregivers. I have included the logo on by brochure, so incorporating the same or similar colors would be fantastic. A trifold brochure would probably be best to fit all the information, as this is a new business and needs to convey all the information in a way that people will read.

Target Market(s)

Doctor's offices and caregivers of children with disabilities.

Industry/Entity Type

Health Care

Font styles to use
Serif
Sans Serif

Colors
33a6d7
85acd3
ffffff
33b8a4
86cfc7

Requirements
Must have
• I would like the same colors of the logo incorporated in the brochure design.
Nice to have
• I would like to see the butterfly somehow in the background or used in the design. Also a trifold or two page design would be greatly appreciated as long as the information can fit.

```html
<!DOCTYPE html>
<html lang="en">
<head>
<meta charset="UTF-8">
<title>Pediatric Occupational Therapy Brochure</title>
<link href="https://fonts.googleapis.com/css2?family=Mulish:wght@400;600;700&family=Didact+Gothic&display=swap" rel="stylesheet">
<style>
  :root {
    --page-bg: #dcebec;
    --teal: #5cc2c6;
    --teal-deep: #3fa9ad;
    --teal-light: #86cfc7;
    --heading-teal: #45bcc3;
    --silver-light: #e4e6e8;
    --silver-dark: #b5b9bd;
    --card: #f3f4f5;
    --text: #6e6e6e;
    --heading-grey: #4f5256;
  }
  * { box-sizing: border-box; margin: 0; padding: 0; }
  html, body {
    width: 1200px; height: 900px; overflow: hidden;
    background: var(--page-bg);
  }
  .brochure {
    position: absolute; left: 45px; top: 30px;
    width: 1110px; height: 840px;
    display: flex;
  }
  .panel {
    width: 370px; height: 840px;
    padding: 26px;
  }
  .panel--teal { background: linear-gradient(160deg, var(--teal-light), var(--teal) 45%, var(--teal-deep)); }
  .panel--silver { background: linear-gradient(90deg, var(--silver-dark), var(--silver-light) 20%, #f6f7f8 50%, var(--silver-light) 80%, var(--silver-dark)); }
  .card {
    position: relative;
    width: 100%; height: 100%;
    background: var(--card);
    padding: 24px 22px;
    font-family: "Didact Gothic", sans-serif;
    color: var(--text);
    font-size: 15px; line-height: 20px;
  }
  .heading {
    font-family: "Mulish", sans-serif;
    font-weight: 600;
    text-transform: uppercase;
    color: var(--heading-teal);
    font-size: 20px; line-height: 24px;
    letter-spacing: 0.2px;
  }
  .heading--grey { color: var(--heading-grey); }
  .subheading {
    font-family: "Mulish", sans-serif;
    font-weight: 600; text-transform: uppercase;
    color: var(--heading-teal);
    font-size: 15px; line-height: 20px;
    padding-bottom: 6px;
    border-bottom: 1px solid #d6d8da;
    margin-top: 16px;
  }
  .intro { margin-top: 26px; }
  .section-gap { margin-top: 28px; }
  .goals { list-style: none; margin-top: 8px; }
  .goals li { padding-left: 14px; text-indent: -12px; margin-bottom: 12px; }
  .goals li::before { content: "- "; }
  .conditions { list-style: none; margin-top: 18px; }
  .conditions li { padding-left: 12px; text-indent: -12px; }
  .conditions li::before { content: "- "; }
  .narrow { width: 170px; }
  .brand {
    position: absolute; right: 20px; bottom: 22px;
    display: flex; align-items: center; gap: 8px;
    font-family: "Didact Gothic", sans-serif;
    font-size: 15px; color: var(--heading-teal);
  }
  .brand-dot { width: 22px; height: 22px; border-radius: 50%; background: var(--teal-light); }
</style>
</head>
<body>
<main class="brochure">
  <section class="panel panel--teal">
    <div class="card">
      <h2 class="heading">Elena Marquez,<br>OTR, C/NDT, Owner</h2>
      <p class="intro">My name is Elena and I am a pediatric Occupational Therapist. I was born and raised in the Rio Grande Valley and have provided services to the pediatric and adult population since 2012. I am currently certified in Neuro-Developmental Treatment of Children with Cerebral Palsy and Other Neuromotor Disorders and have had the pleasure of working with children with various disorders and disabilities. I am a dedicated OTR that works with each client and family to develop a specific plan of care to maximize functional ability across all environments.</p>
      <h2 class="heading section-gap">Role of Occupational Therapy with Children</h2>
      <p class="intro">Occupational therapists work with children, who have challenges, to fully participate in normal daily activities. Those challenges may be due to developmental delay, ADD/ADHD, autism, chromosomal differences, injury, trauma, and many others. An occupational therapist evaluates to assess areas of difficulty as well as strengths, and treat the child based on his or her specific needs.</p>
    </div>
  </section>

  <section class="panel panel--silver">
    <div class="card">
      <h2 class="heading heading--grey">Pediatric Occupational Therapy Services</h2>
      <h3 class="subheading">Occupational Therapy Goals</h3>
      <p style="margin-top:16px">A child's occupation is to be a kid! Through the use of play, I can help children acquire the skills needed for the job of living. These include, but are not limited to:</p>
      <ul class="goals">
        <li>Promoting independence in daily living skills - including dress, grooming and feeding</li>
        <li>Facilitating developmental play skills</li>
        <li>Improving fine motor and eye-hand coordination skills</li>
        <li>Improving sensory processing skills such as organization, self-regulation and behavioral state</li>
        <li>Improving visual motor/visual perceptual skills including writing and coloring</li>
        <li>Addressing orthopedic complications and helping to increase function through the use of splinting and taping</li>
        <li class="narrow">Improving balance and coordination skills through play</li>
      </ul>
      <div class="brand"><span class="brand-dot"></span>Bright Steps OT</div>
    </div>
  </section>

  <section class="panel panel--teal">
    <div class="card">
      <h2 class="heading">Conditions that may benefit from Occupational Therapy:</h2>
      <ul class="conditions">
        <li>ADD/ADHD</li>
        <li>Auditory Processing Disorders</li>
        <li>Autism Spectrum Disorders</li>
        <li>Cancer/Leukemia</li>
        <li>Cerebral Palsy</li>
        <li>Congenital Heart Disease</li>
        <li>Developmental Delay</li>
        <li>Failure to Thrive</li>
        <li>Genetic Disorders/Birth Defects</li>
        <li>Hemophilia</li>
        <li>Neurological Disorders</li>
        <li>Orthopedic Injuries or Surgery</li>
        <li>Sensory Integration Disorders</li>
        <li>Trauma Brain Injuries</li>
        <li>Tracheostomy and/or ventilator dependency</li>
        <li>And any condition that affects a child's growth and development</li>
      </ul>
      <h2 class="heading section-gap">Parental Involvement:</h2>
      <p class="intro">Each child's success is strongly dependent upon the caregiver's involvement. Therapy does not stop when the session ends and must be carried over across all environments in a child's life. I specialize in working with parents and caregivers to ensure home programs are in place to make each child's progress the best.</p>
    </div>
  </section>
</main>
</body>
</html>
```